Realtor/Real Estate Investor Business Card Design

We need a business card design for a new real estate company in Maryland. We buy houses, fix and sell. We do wholesaling as well. We also rent houses.We would like to have blue background and white font.
Updates

Hi All,
I thank all of you for your efforts. You are all experts in designing.
Looking forward to meeting you online in the near future.
mira

Industry/Entity Type

Real Estate

Contact Information for Business Card

Mira Talvek
Real Estate Professional
mira@brightlanehomes.example
301-555-0148
Bright Lane Homes.com

Requirements
Must have
• House picture, and logo at the back of the card
We simplify your buying and selling real estate. at the back of the card

```html
<!DOCTYPE html>
<html lang="en">
<head>
<meta charset="utf-8">
<title>Mira Talvek – Business Card</title>
<link rel="stylesheet" href="https://fonts.googleapis.com/css2?family=Forum&family=Arimo:wght@400&display=swap">
<style>
  :root {
    --stage: #4dbd8f;
    --card-white: #ffffff;
    --brand-blue: #4a8bcb;
    --title-blue: #3f7fc2;
    --ink: #2b2b2b;
    --accent-green: #5cc08e;
    --on-blue: #ffffff;
  }
  * { box-sizing: border-box; margin: 0; padding: 0; }
  html, body {
    width: 1200px; height: 968px; overflow: hidden;
    background: var(--stage);
  }
  .stage {
    position: relative; width: 1200px; height: 968px;
    display: flex; flex-direction: column; align-items: center;
    justify-content: center; gap: 64px;
  }
  .card {
    position: relative; width: 588px; height: 336px;
    overflow: hidden;
    box-shadow: 0 10px 24px rgba(0,0,0,0.18);
  }

  /* Front */
  .card-front { background: var(--card-white); }
  .card-title {
    position: absolute; left: 34px; top: 22px;
    font-family: "Forum", serif; font-weight: 400; font-size: 27px;
    color: var(--title-blue); letter-spacing: 0.2px; white-space: nowrap;
  }
  .contact-list {
    position: absolute; left: 48px; top: 86px;
    list-style: none;
    font-family: "Arimo", sans-serif; font-size: 13px; color: var(--ink);
  }
  .contact-item { height: 33px; }
  .contact-item svg { display: block; width: 14px; height: 14px; margin-bottom: 3px; }
  .contact-item span { display: block; padding-left: 2px; line-height: 15px; }
  .contact-item:nth-child(3) span,
  .contact-item:nth-child(4) span { padding-left: 12px; }
  .brand-mark {
    position: absolute; right: 44px; top: 106px;
    display: flex; align-items: center; gap: 8px;
    font-family: "Arimo", sans-serif; font-size: 16px; color: var(--title-blue);
  }
  .brand-mark .dot {
    width: 12px; height: 12px; border-radius: 50%;
    border: 1.5px solid var(--title-blue);
  }
  .skyline {
    position: absolute; left: 0; right: 0; bottom: 50px; height: 28px;
    background: linear-gradient(to top, var(--brand-blue) 30%, rgba(74,139,203,0.25));
  }
  .base-band {
    position: absolute; left: 0; right: 0; bottom: 0; height: 50px;
    background: var(--brand-blue);
  }

  /* Back */
  .card-back {
    background: var(--brand-blue);
    display: flex; flex-direction: column; align-items: center;
  }
  .back-brand {
    margin-top: 96px;
    display: flex; align-items: center; gap: 12px;
    font-family: "Forum", serif; font-size: 30px; color: var(--on-blue);
  }
  .back-brand .dot {
    width: 26px; height: 26px; border-radius: 50%;
    background: var(--accent-green);
  }
  .tagline {
    position: absolute; bottom: 56px; width: 100%; text-align: center;
    font-family: "Forum", serif; font-size: 19px; color: var(--on-blue);
  }
</style>
</head>
<body>
<main class="stage">
  <section class="card card-front">
    <h1 class="card-title">Mira Talvek Real Estate Professional</h1>
    <ul class="contact-list">
      <li class="contact-item">
        <svg viewBox="0 0 14 14" aria-hidden="true"><path d="M1 7 L7 1.5 L13 7 H11 V13 H3 V7 Z" fill="var(--brand-blue)"/></svg>
        <span>Your adress</span>
      </li>
      <li class="contact-item">
        <svg viewBox="0 0 14 14" aria-hidden="true"><path d="M3 1 L5.5 1 L6.5 4.5 L5 5.7 C5.8 7.6 6.6 8.4 8.3 9.1 L9.5 7.6 L13 8.6 V11 C13 12.2 12 13 10.8 12.9 C5.6 12.3 1.7 8.4 1.1 3.2 C1 2 1.8 1 3 1 Z" fill="var(--brand-blue)"/></svg>
        <span>301-555-0148</span>
      </li>
      <li class="contact-item">
        <svg viewBox="0 0 14 14" aria-hidden="true"><circle cx="7" cy="7" r="5.5" fill="none" stroke="var(--brand-blue)" stroke-width="2"/><circle cx="7" cy="7" r="2" fill="var(--brand-blue)"/></svg>
        <span>mira@brightlanehomes.example</span>
      </li>
      <li class="contact-item">
        <svg viewBox="0 0 14 14" aria-hidden="true"><circle cx="7" cy="7" r="6" fill="var(--brand-blue)"/><path d="M1 7 H13 M7 1 C4 4 4 10 7 13 C10 10 10 4 7 1" fill="none" stroke="#fff" stroke-width="0.9"/></svg>
        <span>brightlanehomes.example</span>
      </li>
    </ul>
    <div class="brand-mark"><i class="dot"></i>Bright Lane Homes</div>
    <div class="skyline" role="img" aria-label="City skyline silhouette"></div>
    <div class="base-band"></div>
  </section>

  <section class="card card-back">
    <div class="back-brand"><i class="dot"></i>Bright Lane Homes</div>
    <p class="tagline">We simplify your buying and selling real estate</p>
  </section>
</main>
</body>
</html>
```